We need a poster designed for use on facebook, as well as to print out for advertising in local noticeboards and shop windows.
The poster will advertise the Fernhollow Turf Society 30th Anniversary Ball.
the ball will be held on the 28th April 2018 at the Fernhollow Community Hall.
Time will be 630pm till late. Ticket Price is $120 which includes 3 course dinner, drinks on arrival and entertainment during the evening.
Additional details will need to be added to the poster at a later date.
The fernhollow Turf Society is a horse racing club run by the community. The club has been incorporateds for 30 years. This Ball will be a celebration of that anniversary.

Target Market(s)

Middlemount Community

Industry/Entity Type

Club

Font styles to use
Serif
Decorative

Colors
1b1b1b
fbfbfb
6b449b
886aae
a64599
ffc214

Requirements
Must have
• Include
• where when time and cost
• ticket inclusions
• entertainement by Colin Hartwell
Nice to have
• Attached are some images for inspiration.
• It would be nice to have the race club logo included somewhere however not prominant.
Should not have
• Abstract geometriic lines
• images of people
• primary colours

```html
<!DOCTYPE html>
<html lang="en">
<head>
<meta charset="utf-8">
<title>Fernhollow Turf Society 30th Anniversary Ball</title>
<link rel="stylesheet" href="https://fonts.googleapis.com/css2?family=Archivo+Black&family=Great+Vibes&family=Roboto+Condensed:wght@400;700&display=swap">
<style>
  :root {
    --ink: #1b1b1b;
    --paper: #fbfbfb;
    --purple: #6b449b;
    --lavender: #886aae;
    --magenta: #a64599;
    --orchid: #d45fd0;
    --gold: #ffc214;
    --gold-deep: #b8860b;
    --gold-light: #ffe27a;
  }
  * { margin: 0; padding: 0; box-sizing: border-box; }
  html, body { width: 968px; height: 1200px; overflow: hidden; background: var(--ink); }
  .poster {
    position: relative; width: 968px; height: 1200px; overflow: hidden;
    font-family: "Roboto Condensed", Arial, sans-serif; color: var(--paper);
  }
  .damask-backdrop {
    position: absolute; inset: 0;
    background: radial-gradient(ellipse at 50% 45%, #3c3c3c 0%, #262626 55%, #161616 100%);
  }
  .dotted-frame { position: absolute; inset: 0; }
  .corner-flourish {
    position: absolute; width: 110px; height: 100px;
    background: radial-gradient(circle at 30% 30%, rgba(255,194,20,.55), rgba(255,194,20,.12) 60%, transparent 75%);
  }
  .corner-flourish.top-left { top: 18px; left: 18px; }
  .corner-flourish.top-right { top: 18px; right: 18px; transform: scaleX(-1); }
  .corner-flourish.bottom-left { bottom: 18px; left: 18px; transform: scaleY(-1); }
  .corner-flourish.bottom-right { bottom: 18px; right: 18px; transform: scale(-1,-1); }

  .presenter { position: absolute; top: 48px; width: 100%; text-align: center; color: var(--gold); }
  .presenter-name { font-weight: 700; font-size: 25px; letter-spacing: .3px; }
  .presenter-note { font-size: 21px; margin-top: 2px; }

  .star-row { position: absolute; top: 138px; left: 0; width: 100%; }

  .laurel-wreath {
    position: absolute; left: 166px; top: 200px; width: 638px; height: 560px;
    border-radius: 50% 50% 45% 45%;
    background: radial-gradient(ellipse at 50% 48%, transparent 40%, rgba(255,194,20,.35) 55%, rgba(184,134,11,.18) 68%, transparent 74%);
  }

  .anniversary-number {
    position: absolute; top: 240px; width: 100%; text-align: center;
    font-family: "Archivo Black", "Arial Black", sans-serif; font-size: 330px; line-height: 1;
    letter-spacing: -6px;
    background: linear-gradient(160deg, var(--gold-light) 0%, var(--gold) 35%, var(--gold-deep) 55%, var(--gold) 75%, var(--gold-light) 100%);
    -webkit-background-clip: text; background-clip: text; color: transparent;
  }
  .ordinal {
    position: absolute; left: 690px; top: 290px; font-size: 30px; color: var(--gold);
    font-family: "Roboto Condensed", Arial, sans-serif;
  }

  .title-ribbon { position: absolute; left: 86px; top: 560px; width: 740px; height: 170px; }
  .ribbon-title {
    position: absolute; left: 0; top: 590px; width: 968px; text-align: center;
    font-family: "Great Vibes", cursive; font-size: 64px; color: var(--paper);
    transform: rotate(-5deg);
  }

  .date-banner { position: absolute; left: 232px; top: 810px; width: 504px; height: 70px; }
  .event-date {
    position: absolute; top: 814px; width: 100%; text-align: center;
    font-weight: 700; font-size: 46px; line-height: 62px; color: var(--paper);
  }
  .event-date sup { font-size: 26px; vertical-align: 16px; }

  .venue-town {
    position: absolute; top: 884px; width: 100%; text-align: center;
    font-weight: 700; font-size: 72px; line-height: 1; letter-spacing: .5px;
  }
  .venue-line {
    position: absolute; top: 950px; width: 100%; text-align: center;
    font-size: 36px; line-height: 1;
  }
  .venue-line .divider { color: var(--gold); margin: 0 16px; }

  .inclusions {
    position: absolute; left: 170px; top: 1034px; width: 200px; text-align: center;
    font-size: 18px; line-height: 1.25;
  }
  .inclusions strong { display: block; font-size: 23px; }

  .ticket-badge {
    position: absolute; left: 408px; top: 1000px; width: 148px; height: 148px; border-radius: 50%;
    border: 4px solid var(--magenta);
    background: radial-gradient(circle at 40% 35%, var(--gold-light), var(--gold) 55%, var(--gold-deep));
    box-shadow: 0 0 0 6px var(--ink);
    display: flex; flex-direction: column; align-items: center; justify-content: center;
    color: var(--paper);
  }
  .ticket-label { font-weight: 700; font-size: 13px; color: var(--ink); }
  .ticket-price { font-weight: 700; font-size: 48px; line-height: 1; }

  .club-mark {
    position: absolute; left: 640px; top: 1030px; width: 190px;
    display: flex; align-items: center; gap: 10px;
  }
  .club-dot { width: 22px; height: 22px; border-radius: 50%; background: var(--purple); flex: none; }
  .club-name { font-weight: 700; font-size: 22px; line-height: 1.1; color: var(--gold); }
</style>
</head>
<body>
<main class="poster">
  <div class="damask-backdrop" role="img" aria-label="Dark damask pattern background"></div>

  <svg class="dotted-frame" width="968" height="1200" viewBox="0 0 968 1200" aria-hidden="true">
    <rect x="36" y="36" width="896" height="1128" fill="none" stroke="#ffc214" stroke-width="3" stroke-dasharray="1 7" stroke-linecap="round"/>
  </svg>

  <div class="corner-flourish top-left" role="img" aria-label="Gold corner flourish"></div>
  <div class="corner-flourish top-right" role="img" aria-label="Gold corner flourish"></div>
  <div class="corner-flourish bottom-left" role="img" aria-label="Gold corner flourish"></div>
  <div class="corner-flourish bottom-right" role="img" aria-label="Gold corner flourish"></div>

  <header class="presenter">
    <p class="presenter-name">FERNHOLLOW TURF SOCIETY</p>
    <p class="presenter-note">PRESENTS</p>
  </header>

  <svg class="star-row" width="968" height="50" viewBox="0 0 968 50" aria-hidden="true">
    <defs>
      <polygon id="star" points="0,-10 2.9,-4 9.5,-3.1 4.7,1.5 5.9,8.1 0,5 -5.9,8.1 -4.7,1.5 -9.5,-3.1 -2.9,-4"/>
    </defs>
    <g fill="#ffc214">
      <use href="#star" transform="translate(413 35) scale(.9)"/>
      <use href="#star" transform="translate(444 27) scale(1.2)"/>
      <use href="#star" transform="translate(484 22) scale(2)"/>
      <use href="#star" transform="translate(524 27) scale(1.2)"/>
      <use href="#star" transform="translate(555 35) scale(.9)"/>
    </g>
  </svg>

  <div class="laurel-wreath" role="img" aria-label="Gold laurel wreath"></div>

  <h1 class="anniversary-number">30</h1>
  <span class="ordinal">th</span>

  <svg class="title-ribbon" viewBox="0 0 740 170" aria-hidden="true">
    <defs>
      <linearGradient id="ribbonFill" x1="0" y1="0" x2="0" y2="1">
        <stop offset="0" stop-color="#d45fd0"/>
        <stop offset="1" stop-color="#a64599"/>
      </linearGradient>
    </defs>
    <path d="M10 90 L70 70 L60 110 L100 128 L40 145 Z" fill="#7d2f73"/>
    <path d="M730 70 L670 60 L680 100 L640 112 L700 125 Z" fill="#7d2f73"/>
    <path d="M70 60 Q370 -10 690 50 L680 110 Q370 60 80 130 Z" fill="url(#ribbonFill)" stroke="#ffc214" stroke-width="2"/>
  </svg>
  <p class="ribbon-title">Anniversary Ball</p>

  <svg class="date-banner" viewBox="0 0 504 70" aria-hidden="true">
    <path d="M0 35 L22 0 H482 L504 35 L482 70 H22 Z" fill="#886aae"/>
    <path d="M14 35 L30 6 H474 L490 35 L474 64 H30 Z" fill="#6b449b"/>
  </svg>
  <p class="event-date">28<sup>TH</sup> APRIL 2018</p>

  <p class="venue-town">FERNHOLLOW</p>
  <p class="venue-line">COMMUNITY HALL<span class="divider">|</span>6:30PM</p>

  <p class="inclusions"><strong>3 COURSE DINNER</strong>DRINKS ON ARRIVAL &amp; ENTERTAINMENT DURING THE EVENING</p>

  <div class="ticket-badge">
    <span class="ticket-label">TICKET PRICE</span>
    <span class="ticket-price">$120</span>
  </div>

  <div class="club-mark">
    <span class="club-dot"></span>
    <span class="club-name">FERNHOLLOW TURF SOCIETY</span>
  </div>
</main>
</body>
</html>
```